Sports Psychology Business Card Design

Need a catchy and unique business card design for our sport psychology practice. We provide mental performance counseling and consulting to performers from all types of industries with a special emphases on athletes.The name of our practice is "Inner Edge of Excellence" or "IEE" as is indicated in the logo examples submitted in this brief. Also provided were logos with specific sports referenced which represent sources of our clients from those sports.

Target Market(s)

Executives, Professionals (doctors, lawyers, etc.), Athletes, Entertainers and other performers

Contact Information for Business Card

Need to include our logo (logos provided in this brief).

Font styles to use
Other font styles liked:
• Font can be found in logo

Colors
0792cd
34a7d8
85cae6

Requirements
Must have
• Our logo and reference to our provision of mental performance counseling/consulting/coaching
Nice to have
• References to sports that our athletes play as provided in the brief.
Should not have
• This is not a general wellness consulting practice. Our focus is on consulting to improve mental performance.

```html
<!DOCTYPE html>
<html lang="en">
<head>
<meta charset="UTF-8">
<title>Inner Edge of Excellence – Business Card</title>
<link href="https://fonts.googleapis.com/css2?family=Orbitron:wght@600;800&family=Montserrat:wght@400;500&display=swap" rel="stylesheet">
<style>
  :root{
    --blue:#0792cd;
    --blue-mid:#34a7d8;
    --blue-light:#85cae6;
    --ink:#22272b;
    --black:#050505;
    --badge:#141414;
    --white:#ffffff;
    --backdrop:#e6e9eb;
  }
  *{margin:0;padding:0;box-sizing:border-box}
  html,body{width:1200px;height:900px;overflow:hidden;background:var(--backdrop)}
  .canvas{position:relative;width:1200px;height:900px}
  .card{position:absolute;left:320px;width:560px;height:320px;overflow:hidden;box-shadow:0 6px 18px rgba(0,0,0,.18)}
  .card--front{top:95px}
  .card--back{top:485px;background:var(--black)}
  .front-shape{position:absolute;inset:0}
  .contact{position:absolute;left:0;top:34px;color:var(--white);font-family:"Montserrat",sans-serif}
  .contact__name{font-family:"Orbitron",sans-serif;font-weight:800;font-size:22px;letter-spacing:1px;margin-left:36px;text-transform:uppercase}
  .contact__role{font-size:10px;letter-spacing:1.6px;margin-left:36px;margin-top:2px;text-transform:uppercase}
  .contact__list{list-style:none;margin-top:26px}
  .contact__item{display:flex;align-items:center;height:30px;margin-bottom:6px;font-size:11px;letter-spacing:.3px;white-space:nowrap}
  .contact__tab{width:58px;height:24px;background:var(--white);border-radius:0 12px 12px 0;display:flex;align-items:center;justify-content:flex-end;padding-right:6px;margin-right:16px}
  .contact__web{position:absolute;left:150px;top:260px;color:var(--white);font-family:"Montserrat",sans-serif;font-size:11.5px;letter-spacing:.6px}
  .brand{position:absolute;left:372px;right:0;top:130px;text-align:center}
  .brand__name{font-family:"Orbitron",sans-serif;font-weight:800;font-size:48px;color:var(--ink);letter-spacing:2px}
  .tagline{position:absolute;left:0;right:0;top:58px;text-align:center;font-family:"Orbitron",sans-serif;font-weight:800;text-transform:uppercase;line-height:1}
  .tagline__the{color:var(--blue-light);font-size:26px;letter-spacing:2px}
  .tagline__main{color:var(--blue);font-size:46px;letter-spacing:1px;margin-top:6px}
  .tagline__sub{color:var(--white);font-size:20px;letter-spacing:2px;margin-top:10px;font-weight:600}
  .sports{position:absolute;left:0;right:0;bottom:40px;display:flex;justify-content:center;gap:18px}
  .sports__badge{width:132px;height:44px;background:var(--badge)}
</style>
</head>
<body>
<main class="canvas">
  <section class="card card--front" aria-label="Card front">
    <svg class="front-shape" width="560" height="320" viewBox="0 0 560 320">
      <defs>
        <linearGradient id="panelBlue" x1="0" y1="0" x2="1" y2="1">
          <stop offset="0" stop-color="#0d86cf"/>
          <stop offset="1" stop-color="#1a95d6"/>
        </linearGradient>
      </defs>
      <rect width="560" height="320" fill="url(#panelBlue)"/>
      <path d="M414,0 C324,80 310,250 346,320 L560,320 L560,0 Z" fill="var(--blue-mid)"/>
      <path d="M430,0 C344,86 332,250 370,320 L560,320 L560,0 Z" fill="var(--white)"/>
    </svg>
    <div class="contact">
      <div class="contact__name">Dana Whitcombe</div>
      <div class="contact__role">Mental Performance Consultant</div>
      <ul class="contact__list">
        <li class="contact__item"><span class="contact__tab">
          <svg width="14" height="14" viewBox="0 0 14 14"><path d="M7,1 C4.5,1 3,2.8 3,5 C3,8 7,13 7,13 C7,13 11,8 11,5 C11,2.8 9.5,1 7,1 Z" fill="var(--blue)"/><circle cx="7" cy="5" r="1.6" fill="var(--white)"/></svg>
        </span>4580, Harbor Lane, Springfield USA 40210</li>
        <li class="contact__item"><span class="contact__tab">
          <svg width="14" height="14" viewBox="0 0 14 14"><rect x="1" y="3" width="12" height="8" fill="var(--blue)"/><path d="M1,3 L7,8 L13,3" fill="none" stroke="var(--white)" stroke-width="1.2"/></svg>
        </span>dana@inneredge.co</li>
        <li class="contact__item"><span class="contact__tab">
          <svg width="14" height="14" viewBox="0 0 14 14"><path d="M3,1.5 L5.5,1.5 L6.5,4.5 L5,5.8 C5.8,7.6 6.8,8.6 8.4,9.3 L9.7,7.8 L12.5,8.8 L12.5,11.5 C7,12 2.2,7.2 3,1.5 Z" fill="var(--blue)"/></svg>
        </span>555-014-2297</li>
      </ul>
    </div>
    <div class="contact__web">www.inneredge.co</div>
    <div class="brand">
      <span class="brand__name">IEE</span>
    </div>
  </section>

  <section class="card card--back" aria-label="Card back">
    <div class="tagline">
      <div class="tagline__the">The</div>
      <div class="tagline__main">Inner Edge</div>
      <div class="tagline__sub">of Excellence</div>
    </div>
    <div class="sports">
      <span class="sports__badge"></span>
      <span class="sports__badge"></span>
      <span class="sports__badge"></span>
    </div>
  </section>
</main>
</body>
</html>
```